Cover-Design für Office Notizbuch gesucht
Zielgruppe
Wir erstellen schöne Officeprodukte für junge, modebewusste (und alte) Mädels. Es soll also sehr quillorat / moranteve tauglich sein.
Aufgabenstellung
Wir möchten ein Din A5 Notizbuch haben und suchen dafür ein tolles Coverdesign.
Es soll ein zeitloses Design haben, gerne mit einem motivierenden Spruch oder einfach einem schönen Muster und Design.
Zusätzlich kann auch mit einer Heißfolienprägung Gold gearbeitet werden.

```html
<!DOCTYPE html>
<html lang="de">
<head>
<meta charset="utf-8">
<title>Notes – Notizbuch Cover</title>
<link rel="stylesheet" href="https://fonts.googleapis.com/css2?family=Josefin+Sans:wght@300&display=swap">
<style>
  :root {
    --backdrop: #fbe9df;
    --marble-light: #fbfbfb;
    --marble-mid: #ececec;
    --marble-vein: #e9d3cf;
    --panel-grey: #e4e2e3;
    --rose: #d3a5a5;
    --cover-text: #ffffff;
  }
  html, body {
    margin: 0;
    padding: 0;
    overflow: hidden;
  }
  body {
    width: 1200px;
    height: 1105px;
    background: var(--backdrop);
    display: flex;
    align-items: center;
    justify-content: center;
  }
  .notebook-cover {
    position: relative;
    width: 560px;
    height: 792px;
    box-shadow: 0 18px 40px rgba(150, 110, 95, 0.18);
    overflow: hidden;
  }
  .cover-art {
    position: absolute;
    inset: 0;
    display: block;
  }
  .cover-title {
    position: absolute;
    right: 38px;
    bottom: 74px;
    margin: 0;
    font-family: "Josefin Sans", sans-serif;
    font-weight: 300;
    font-size: 46px;
    letter-spacing: 0.14em;
    color: var(--cover-text);
  }
</style>
</head>
<body>
  <div class="notebook-cover">
    <svg class="cover-art" width="560" height="792" viewBox="0 0 560 792" xmlns="http://www.w3.org/2000/svg">
      <defs>
        <linearGradient id="marble-tone" x1="0" y1="0" x2="1" y2="1">
          <stop offset="0" stop-color="var(--marble-light)"/>
          <stop offset="0.35" stop-color="var(--marble-mid)"/>
          <stop offset="0.55" stop-color="var(--marble-vein)"/>
          <stop offset="0.8" stop-color="var(--marble-mid)"/>
          <stop offset="1" stop-color="var(--marble-light)"/>
        </linearGradient>
      </defs>
      <rect class="marble-surface" x="0" y="0" width="560" height="792" fill="url(#marble-tone)" role="img" aria-label="Weißer Marmor mit feinen roségoldenen Adern"/>
      <polygon class="grey-panel" points="0,700 240,663 95,792 0,792" fill="var(--panel-grey)"/>
      <polygon class="rose-panel" points="560,380 560,792 95,792" fill="var(--rose)"/>
    </svg>
    <p class="cover-title">NOTES</p>
  </div>
</body>
</html>
```